Identity Package (Logo, Website)

We need a logo and website design for a new company.
The new company is a voicemail transcription service provider. It's name is KL9BQZ.io
It will be very transactional. We like the "bootstrap" look and feel, and will be using a developer familiar with bootstrap. Here are the kinds of webpages we like :
https://www.lumenvane.io
http://www.quorbil.com/
http://www.plenivo.com/
There will only be 5 pages, as follows :
1- Homepage
2- Voicemail Transcription for Individuals
3- Voicemail Transcription for Companies
4- Wholesale Voicemail Transcription for Service Providers/Enterprises
5- Contact us
As far as the logo is concerned, we'd like to have just stylized text. It should be done in such a way as to make it easy to see the different elements of the name, which are KL, 2, and BQZ.
Reason: I have received a number of designs, but the designs are mostly from the same few designers (not that much variety in designers). I'd like a few more to compare if possible, so I thought I would keep this open until Monday to give more designers the opportunity to submit over the weekend. Thanks!

```html
<!DOCTYPE html>
<html lang="en">
<head>
<meta charset="utf-8">
<title>KL2BQZ – Voicemail Transcription</title>
<link rel="stylesheet" href="https://fonts.googleapis.com/css2?family=Open+Sans:wght@400;600;700&family=Russo+One&family=PT+Sans:wght@700&family=Arimo:wght@400;700&family=Oswald:wght@300&display=swap">
<style>
:root{
  --navy:#265a78;
  --hero-blue:#1f5c85;
  --teal:#7bc0a7;
  --green-name:#5aa889;
  --yellow:#fcc60b;
  --footer:#4a6272;
  --ink:#333;
  --muted:#555;
  --white:#fff;
}
*{margin:0;padding:0;box-sizing:border-box}
html,body{width:1200px;height:2748px;overflow:hidden}
body{position:relative;font-family:"Open Sans",Arial,sans-serif;background:var(--white);color:var(--ink)}
section,header,footer{position:absolute;left:0;width:1200px}
.abs{position:absolute}

/* header */
.site-header{top:0;height:92px;background:var(--navy)}
.brand{left:33px;top:20px;display:flex;align-items:center;gap:12px;color:var(--white);font-weight:600;font-size:44px;line-height:1}
.brand-dot{width:50px;height:50px;border-radius:50%;background:var(--white)}
.nav{top:38px;font-family:Arimo,Arial,sans-serif;font-size:17px;color:var(--white);letter-spacing:.3px}
.nav-login{left:1070px;top:33px;width:90px;height:35px;border-radius:9px;background:var(--yellow);color:var(--navy);font-family:Arimo,sans-serif;font-size:17px;text-align:center;line-height:35px}

/* hero */
.hero{top:92px;height:591px}
.hero-photo{position:absolute;inset:0;background:
  radial-gradient(ellipse 60% 90% at 88% 40%,#1a120e 0%,#2a1e18 45%,rgba(60,40,30,0) 75%),
  radial-gradient(ellipse 70% 70% at 15% 75%,#f3b47a 0%,rgba(243,180,122,0) 70%),
  linear-gradient(180deg,#e8cfe4 0%,#f2d5d6 40%,#e7a277 75%,#6b3f2a 100%)}
.hero-title{left:31px;top:82px;font-family:"Russo One",sans-serif;font-style:italic;font-size:45px;color:var(--hero-blue);letter-spacing:1px;line-height:1}
.hero-sub{left:31px;top:136px;font-family:"Russo One",sans-serif;font-style:italic;font-size:27px;color:var(--hero-blue);letter-spacing:1px;line-height:1}
.hero-text{left:31px;top:178px;width:530px;font-size:20px;line-height:24px;color:#2b2b2b}

/* intro */
.intro{top:683px;height:383px;text-align:center}
.intro h1{position:absolute;left:0;width:1200px;top:98px;font-size:44px;font-weight:700;color:var(--navy)}
.intro p{position:absolute;left:165px;width:870px;top:176px;font-size:29px;line-height:36px;color:var(--muted)}

/* services */
.services{top:1066px;height:559px;background:var(--teal)}
.service{position:absolute;top:0;width:330px;color:var(--white)}
.service-card{position:absolute;top:83px;left:31px;width:260px;height:154px;background:var(--white);border-radius:6px}
.service-card::after{content:"";position:absolute;left:50%;bottom:-14px;margin-left:-14px;border:14px solid transparent;border-bottom:0;border-top-color:var(--white)}
.service-card svg{position:absolute;left:50%;top:50%;transform:translate(-50%,-50%)}
.service h2{position:absolute;top:277px;left:0;width:322px;text-align:center;font-size:25px;line-height:30px;font-weight:700}
.service p{position:absolute;width:330px;font-size:17px;line-height:20px}

/* testimonials */
.testimonials{top:1625px;height:625px}
.testimonials h2{position:absolute;top:78px;width:1200px;text-align:center;font-family:"PT Sans",sans-serif;font-size:49px;color:var(--ink)}
.quote{position:absolute;top:234px;padding-top:165px}
.avatar{position:absolute;top:0;width:122px;height:122px;border-radius:50%;background:radial-gradient(circle at 50% 40%,#e8cdb8 0%,#d9c7b8 55%,#f1ebe4 100%)}
.quote p{font-family:Arimo,Arial,sans-serif;font-size:18px;line-height:20px;color:var(--ink)}
.quote .name{display:block;margin-top:8px;font-family:Arimo,sans-serif;font-weight:700;font-size:20px;line-height:24px;color:var(--green-name)}
.quote .role{display:block;font-family:Arimo,sans-serif;font-size:14px;line-height:18px;color:#888}

/* call to action */
.cta{top:2250px;height:220px;background:var(--yellow);text-align:center}
.cta p{position:absolute;top:36px;width:1200px;font-size:37px;color:var(--white)}
.cta-btn{position:absolute;left:458px;top:106px;width:284px;height:79px;background:var(--white);display:flex;align-items:center;justify-content:center;gap:20px;font-size:26px;font-weight:700;color:var(--yellow)}

/* footer */
.site-footer{top:2470px;height:278px;background:var(--footer);color:var(--white)}
.footer-brand{left:33px;top:68px;display:flex;align-items:center;gap:10px;font-weight:600;font-size:40px;line-height:1}
.footer-brand .brand-dot{width:44px;height:44px}
.copyright{left:33px;top:128px;font-family:Arimo,sans-serif;font-size:14px}
.footer-h{top:70px;font-size:23px;font-weight:700;letter-spacing:-.3px}
.social{top:118px;left:339px;display:flex;gap:15px}
.social span{width:55px;height:55px;border-radius:50%;background:#dfe6ea}
.footer-links{top:120px;list-style:none;font-family:Arimo,sans-serif;font-size:17px;line-height:19.5px}
.address{left:940px;top:118px;font-family:Arimo,sans-serif;font-size:15.5px;line-height:21px;white-space:nowrap}
.phone{left:936px;top:160px;display:flex;align-items:center;gap:8px;font-family:Oswald,sans-serif;font-weight:300;font-size:38px}
</style>
</head>
<body>

<header class="site-header">
  <div class="abs brand"><span class="brand-dot"></span>kl2bqz</div>
  <span class="abs nav" style="left:623px">FEATURES</span>
  <span class="abs nav" style="left:751px">PRICING</span>
  <span class="abs nav" style="left:857px">LEARNING</span>
  <span class="abs nav" style="left:982px">SIGN UP</span>
  <span class="abs nav-login">LOGIN</span>
</header>

<section class="hero">
  <div class="hero-photo" role="img" aria-label="Businessman in a suit holding out a mobile phone, a suspension bridge glowing at sunset behind him"></div>
  <div class="abs hero-title">YOUR NO.1 VOICEMAIL</div>
  <div class="abs hero-sub">TRANSCRIPTION SERVICE PROVIDER</div>
  <p class="abs hero-text">Duis autem vel eum iriure dolor in hendrerit in vulputate velit esse molestie consequat, vel illum dolore eu feugiat nulla facilisis at vero eros et accumsan et iusto odio.</p>
</section>

<section class="intro">
  <h1>Lorem ipsum dolor sit amet consectetuer</h1>
  <p>Ut wisi enim ad minim veniam, quis nostrud exerci tation ullamcorper suscipit lobortis nisl ut aliquip ex ea commodo consequat.</p>
</section>

<section class="services">
  <div class="service" style="left:35px">
    <div class="service-card">
      <svg width="50" height="100" viewBox="0 0 50 100" fill="var(--teal)">
        <circle cx="25" cy="12" r="10"/>
        <path d="M7 26h36l2 36h-8v36h-8V62h-8v36h-8V62H5z"/>
      </svg>
    </div>
    <h2>Voicemail Transcription<br>for Individuals</h2>
    <p style="top:362px;left:5px">Typi non habent claritatem insitam est usus legentis in iis qui facit eorum claritatem. Investigationes demonstraverunt lectores legere me lius quod ii legunt saepius.</p>
  </div>
  <div class="service" style="left:440px">
    <div class="service-card">
      <svg width="100" height="100" viewBox="0 0 100 100" fill="var(--teal)">
        <ellipse cx="50" cy="86" rx="40" ry="9" fill="none" stroke="var(--teal)" stroke-width="4"/>
        <circle cx="50" cy="10" r="8"/><path d="M38 22h24l2 30h-6v30h-16V52h-6z"/>
        <circle cx="20" cy="30" r="6"/><path d="M11 40h18l2 22h-5v20h-12V62h-5z"/>
        <circle cx="80" cy="30" r="6"/><path d="M71 40h18l2 22h-5v20h-12V62h-5z"/>
      </svg>
    </div>
    <h2>Voicemail Transcription<br>for Companies</h2>
    <p style="top:362px;left:2px">Typi non habent claritatem insitam est usus legentis in iis qui facit eorum claritatem. Investigationes demonsrunt lectores legere me lius quod ii l.</p>
  </div>
  <div class="service" style="left:835px">
    <div class="service-card">
      <svg width="104" height="104" viewBox="0 0 104 104" fill="none" stroke="var(--teal)" stroke-width="5">
        <circle cx="52" cy="52" r="44"/>
        <ellipse cx="52" cy="52" rx="20" ry="44"/>
        <path d="M8 52h88M16 30h72M16 74h72"/>
        <circle cx="52" cy="8" r="6" fill="var(--teal)"/>
        <circle cx="92" cy="36" r="6" fill="var(--teal)"/>
        <circle cx="12" cy="36" r="6" fill="var(--teal)"/>
      </svg>
    </div>
    <h2>Voicemail Transcription<br>for Service Providers /<br>Enterprises</h2>
    <p style="top:397px;left:8px">Typi non habent claritatem insitam est usus legentis in iis qui facit eorum claritatem. Investigationes demonstrnt lectores legere me lius quod ii legunt.</p>
  </div>
</section>

<section class="testimonials">
  <h2>What People Say About KL2BQZ</h2>
  <div class="quote" style="left:38px;width:335px">
    <div class="avatar" style="left:83px" role="img" aria-label="Portrait photo of a smiling customer"></div>
    <p>Vel illum dolore eu feugiat nulla facilisis at vero eros et accumsan et iusto dignissim qui blandit praesent lupt zril delenit augue duis dolore te feugait nulla facilisi.</p>
    <span class="name">Dorian Halvesten</span>
    <span class="role">Accounting &nbsp;Officer</span>
  </div>
  <div class="quote" style="left:429px;width:385px">
    <div class="avatar" style="left:87px" role="img" aria-label="Portrait photo of a customer in a suit"></div>
    <p>Typi non habent claritatem insitam est us legentis in iis qui facit eorum claritatem. Investigationes demonstraverunt lectores legere me lius quod ii legunt saepius.</p>
    <span class="name">Rowan Pellacre</span>
    <span class="role">Accounting &nbsp;Officer</span>
  </div>
  <div class="quote" style="left:832px;width:340px">
    <div class="avatar" style="left:93px" role="img" aria-label="Portrait photo of a smiling businesswoman"></div>
    <p>Claritas est etiam processus dynamicus sequitur mutationem consuetudium lectorum. Mirum est notare quam littera gothica, quam nunc pumus parum clam, anteposuerit litterarum formas.</p>
    <span class="name">Celina Variott</span>
    <span class="role">President, CEO of Nordavex</span>
  </div>
</section>

<section class="cta">
  <p>Create your account today. No credit card required.</p>
  <div class="cta-btn">
    <svg width="40" height="40" viewBox="0 0 40 40">
      <circle cx="20" cy="20" r="20" fill="var(--yellow)"/>
      <path d="M10 20h17M20 12l8 8-8 8" fill="none" stroke="var(--white)" stroke-width="4.5" stroke-linecap="round" stroke-linejoin="round"/>
    </svg>
    GET STARTED
  </div>
</section>

<footer class="site-footer">
  <div class="abs footer-brand"><span class="brand-dot"></span>kl2bqz</div>
  <div class="abs copyright">© 2014 KL2BQZ. All Rights Reserved.</div>

  <div class="abs footer-h" style="left:339px">CONNECT WITH US</div>
  <div class="abs social"><span></span><span></span><span></span></div>

  <div class="abs footer-h" style="left:630px">NAVIGATION</div>
  <ul class="abs footer-links" style="left:632px">
    <li>Home</li><li>About</li><li>Products</li><li>Services</li><li>Brands</li>
  </ul>
  <ul class="abs footer-links" style="left:746px">
    <li>Sitemap</li><li>Webshop</li><li>Terms of Use</li><li>Privacy Policy</li><li>Contact Us</li>
  </ul>

  <div class="abs footer-h" style="left:940px">CONTACT US</div>
  <div class="abs address">#38 street city, state, Country<br>email : info@kestrelpost.com.au</div>
  <div class="abs phone">
    <svg width="32" height="32" viewBox="0 0 32 32" fill="none" stroke="var(--white)" stroke-width="2">
      <circle cx="16" cy="16" r="14"/>
      <path d="M11 8l3 4-2 2c1 3 3 5 6 6l2-2 4 3-2 3c-7 0-14-7-14-14z" fill="var(--white)" stroke="none"/>
    </svg>
    012.555.0148
  </div>
</footer>

</body>
</html>
```